5 Blog Posts and Lead Magnet Needs Branding for Remodeling Company

I have 5 blogs and a website lead magnet that have content written but need some design and layout help to align with my brand identity. The content will need to be formatted for social media and website. I have a logo, colors and font. I also have a website I'm pretty happy with right now that can provide direction.
Target Market(s)
Age 40-65, Average salary 250K, Male/Female Professional College + Married 3 + Mid-full size car with high end finishes.
Industry/Entity Type
Construction, remodeling
Colors
Look and feel

```html
<!DOCTYPE html>
<html lang="en">
<head>
<meta charset="UTF-8">
<title>Tips for Hiring a Remodelling Contractor</title>
<link href="https://fonts.googleapis.com/css2?family=Jost:wght@400;500;600;700&family=League+Spartan:wght@800;900&display=swap" rel="stylesheet">
<style>
  :root {
    --navy: #0c1a4a;
    --coral: #f2a58f;
    --blush: #fbe3df;
    --ghost: #f4f4f4;
    --white: #ffffff;
  }
  * { margin: 0; padding: 0; box-sizing: border-box; }
  html, body { width: 928px; height: 1200px; overflow: hidden; background: var(--white); }
  .sheet {
    position: relative;
    width: 928px;
    height: 1200px;
    overflow: hidden;
    background: var(--white);
    color: var(--navy);
    font-family: "Jost", sans-serif;
  }
  .sheet > * { position: absolute; }

  .ghost-numbers { left: 0; top: 0; z-index: 0; }
  .ghost-numbers text {
    font-family: "League Spartan", sans-serif;
    font-weight: 900;
    font-size: 345px;
    fill: var(--ghost);
  }

  .brand {
    left: 126px;
    top: 26px;
    display: flex;
    align-items: center;
    gap: 10px;
    font-weight: 700;
    color: var(--navy);
    z-index: 1;
  }
  .brand-dot { width: 14px; height: 14px; border-radius: 50%; background: var(--navy); }
  .brand-name { font-size: 36px; line-height: 1; }
  .brand-name small { display: block; font-size: 10px; letter-spacing: 1.6px; margin-top: 6px; }

  .rule { top: 113px; height: 4px; background: var(--coral); }
  .rule--left { left: 61px; width: 275px; }
  .rule--right { left: 580px; width: 275px; }

  .kicker {
    left: 0; width: 928px; top: 92px;
    text-align: center; font-weight: 600;
    font-size: 40px; line-height: 48px; letter-spacing: 3px; color: var(--navy);
    text-indent: 3px;
  }
  .headline { left: 0; top: 0; width: 928px; }
  .headline-top {
    position: absolute; left: 0; width: 928px; top: 146px;
    text-align: center; font-family: "League Spartan", sans-serif; font-weight: 900;
    font-size: 60px; letter-spacing: 6.5px; text-indent: 6.5px; color: var(--coral); line-height: 1;
  }
  .headline-main {
    position: absolute; left: 0; width: 928px; top: 202px;
    text-align: center; font-family: "League Spartan", sans-serif; font-weight: 900;
    font-size: 112px; letter-spacing: 9px; text-indent: 9px; color: var(--navy); line-height: 1;
  }

  .intro {
    left: 40px; width: 848px; top: 307px;
    text-align: center; font-size: 17.5px; line-height: 21.8px; letter-spacing: 1.1px; font-weight: 500;
    z-index: 1;
  }
  .lead-in {
    left: 0; width: 928px; top: 421px;
    text-align: center; font-size: 23px; line-height: 30px; font-weight: 600; letter-spacing: 1.4px;
    z-index: 1;
  }

  .question { top: 495px; width: 240px; z-index: 1; }
  .question--communicate { left: 84px; }
  .question--budget { left: 370px; }
  .question--guarantee { left: 656px; }
  .question-pre, .question-post {
    font-weight: 700; font-size: 14.5px; letter-spacing: 1.5px; line-height: 18px;
  }
  .question-key {
    font-weight: 700; font-size: 26px;
    letter-spacing: 2.2px; color: var(--coral); line-height: 26px;
  }
  .question-body {
    margin-top: 3px; font-size: 14.5px; line-height: 18.9px; letter-spacing: 0.8px; font-weight: 400;
    white-space: nowrap;
  }

  .closing {
    left: 61px; width: 780px; top: 718px;
    font-weight: 700; font-size: 30px; line-height: 36.5px; white-space: nowrap;
    z-index: 1;
  }

  .offer-box {
    left: 58px; top: 888px; width: 712px; height: 156px;
    background: var(--coral);
    z-index: 1;
  }
  .offer-text {
    position: absolute; left: 33px; top: 26px;
    color: var(--white); font-weight: 600; font-size: 20.5px; line-height: 25.5px; white-space: nowrap;
  }

  .cta-band {
    left: 0; top: 1072px; width: 690px; height: 95px;
    background: var(--blush);
    z-index: 1;
  }
  .cta-line { position: absolute; left: 61px; color: var(--navy); font-weight: 700; white-space: nowrap; line-height: 1; }
  .cta-line--small { top: 18px; font-size: 21px; }
  .cta-line--large { top: 42px; font-size: 38px; }

  .corner-disc { left: 0; top: 0; z-index: 2; }
</style>
</head>
<body>
<main class="sheet">
  <svg class="ghost-numbers" width="928" height="1200" viewBox="0 0 928 1200" aria-hidden="true">
    <text x="50" y="709">1</text>
    <text x="305" y="709">2</text>
    <text x="600" y="709">3</text>
  </svg>

  <div class="brand">
    <span class="brand-dot"></span>
    <span class="brand-name">Harlow<small>HOME IMPROVEMENTS</small></span>
  </div>

  <span class="rule rule--left"></span>
  <span class="rule rule--right"></span>
  <h2 class="kicker">TIPS FOR</h2>
  <h1 class="headline">
    <span class="headline-top">HIRING A REMODELLING</span>
    <span class="headline-main">CONTRACTOR</span>
  </h1>

  <p class="intro">During my time as a remodeling contractor I’ve heard a lot of stories of bad remodel<br>experiences. I’ve even learned some hard lessons myself in how to deliver a great client<br>experience. The truth is hiring the right contractor is a critical step in any home renovation<br>project. You want to know that the person or company you hire will not just do the job but do<br>it with the quality and care you deserve.</p>
  <p class="lead-in">Below are three critical questions to ask before hiring a contractor.</p>

  <section class="question question--communicate">
    <p class="question-pre">HOW WILL THEY</p>
    <p class="question-key">COMMUNICATE</p>
    <p class="question-post">WITH YOU?</p>
    <p class="question-body">Address the budget upfront.<br>Request a detailed bid and ask<br>how they handle unexpected<br>costs or changes in scope.<br>Clarify terms regarding<br>deposits and paymen<br>schedules to avoid any</p>
  </section>
  <section class="question question--budget">
    <p class="question-pre">HOW WILL</p>
    <p class="question-key">BUDGETING</p>
    <p class="question-post">BE HANDLED?</p>
    <p class="question-body">Address the budget upfront.<br>Request a detailed bid and ask<br>how they handle unexpected<br>costs or changes in scope.<br>Clarify terms regarding<br>deposits and paymen<br>schedules to avoid any</p>
  </section>
  <section class="question question--guarantee">
    <p class="question-pre">WHAT</p>
    <p class="question-key">GUARANTEES</p>
    <p class="question-post">DO THEY OFFER?</p>
    <p class="question-body">Address the budget upfront.<br>Request a detailed bid and ask<br>how they handle unexpected<br>costs or changes in scope.<br>Clarify terms regarding<br>deposits and paymen<br>schedules to avoid any</p>
  </section>

  <p class="closing">What I’ve covered here is just a small sample of the<br>information you should know to ensure you are<br>well-informed when you get started on the<br>remodel process.</p>

  <div class="offer-box">
    <p class="offer-text">I want to provide you with a guide to avoiding 5 common<br>mistakes when planning your remodeling project. It’s<br>completely FREE, and it will help you to avoid any nasty<br>surprises that can sneak up on you during a remodel.</p>
  </div>

  <div class="cta-band">
    <p class="cta-line cta-line--small">Just click on the link below and let me know what email</p>
    <p class="cta-line cta-line--large">you’d like this FREE guide sent.</p>
  </div>

  <svg class="corner-disc" width="928" height="1200" viewBox="0 0 928 1200" aria-hidden="true">
    <circle cx="1010" cy="1165" r="325" fill="var(--navy)"/>
  </svg>
</main>
</body>
</html>
```